Logo and Label design for e-liquid and a poster for advertising the line

Brand name will be Gloam e-Liquid, emphasis on Gloam and e-Liquid should be subtle. I am thinking about using the biohazard logo/emblem/symbol as the key to the logo. Something kind of dark in nature, maybe some blood splattered across the logo, maybe some radioactive looking liquid dripping from the biohazard symbol. Maybe something implemented into the biohazard symbol like a skull or cool alien face (not the common big eyed simple alien face). We use Tessaro QM720 labels that are 4" x 1.5". We use the free software from Quillmark (Brindle Dynamics) that works on the Tessaro QM720. We are thinking that an ink friendly version (spread the colors out, not heavy on one color) would be nice or having the ability to print the same thing in a few different colors (able to print the label in 3 different color schemes).
We also have to put the following info on the labels; Warning Keep away from children and pets. May be harmful if swallowed. Ingredients: Propylene Glycol, Vegetable Glycerin, Natural and Artificial Flavor, (number)mg Nicotine. The name of the specific liquid. The date bottled. (We use the under 18 with the circle and slash across it for the no one under 18 to save space).
We need to be able to change the date, name, mg of nicotine.
On the poster we need a made in the usa stamp and also the slogan.... Caution: Very Contagious!

Industry/Entity Type

Advertising

Logo Text

Gloam e-Liquid

```html
<!DOCTYPE html>
<html lang="en">
<head>
<meta charset="utf-8">
<title>Gloam e-Liquid – Logo and Label Set</title>
<link rel="stylesheet" href="https://fonts.googleapis.com/css2?family=Archivo+Black&family=Arimo:wght@400;700&display=swap">
<style>
  :root {
    --canvas: #ffffff;
    --ink: #111111;
    --paper: #ffffff;
    --label-red: #c0302b;
    --label-green: #07963f;
    --label-navy: #1b2a40;
    --label-edge: #d9d9d9;
  }
  * { margin: 0; padding: 0; box-sizing: border-box; }
  html, body {
    width: 1200px; height: 961px; overflow: hidden;
    background: var(--canvas);
  }
  .artboard { position: relative; width: 1200px; height: 961px; }

  .brand-name {
    font-family: "Archivo Black", "Arial Black", sans-serif;
    font-weight: 400;
    line-height: 1;
    white-space: nowrap;
  }
  .label-copy {
    font-family: "Arimo", Arial, sans-serif;
    white-space: nowrap;
  }
  .label-copy strong { font-weight: 700; display: block; }
  .emblem {
    position: absolute;
    border-radius: 50%;
    background: currentColor;
  }

  /* Horizontal lockup */
  .lockup-horizontal { position: absolute; inset: 0; color: var(--ink); }
  .lockup-horizontal .brand-name {
    position: absolute; right: 709px; top: 221px; font-size: 30px;
  }
  .lockup-horizontal .label-copy {
    position: absolute; right: 711px; top: 256px;
    text-align: right; font-size: 8.5px; line-height: 1.1;
  }
  .lockup-horizontal .emblem { left: 508px; top: 211px; width: 114px; height: 114px; }

  /* Stacked lockup */
  .lockup-stacked { position: absolute; left: 694px; top: 154px; width: 280px; color: var(--ink); text-align: center; }
  .lockup-stacked .emblem { left: 83px; top: 6px; width: 114px; height: 114px; }
  .lockup-stacked .brand-name { position: absolute; left: -20px; right: -20px; top: 128px; font-size: 30px; }
  .lockup-stacked .label-copy { position: absolute; left: -20px; right: -20px; top: 163px; font-size: 8.5px; line-height: 1.1; }

  /* Label strips */
  .label-strip {
    position: absolute; left: 142px; width: 916px; height: 96px;
    box-shadow: 0 0 0 3px var(--label-edge);
  }
  .label-strip.is-red { top: 438px; background: var(--label-red); }
  .label-strip.is-green { top: 568px; background: var(--label-green); }
  .label-strip.is-navy { top: 698px; background: var(--label-navy); }

  .strip-lockup { position: absolute; top: 0; left: 0; width: 916px; height: 96px; }
  .strip-lockup.is-light { color: var(--paper); }
  .strip-lockup.is-dark { color: var(--ink); }
  .strip-lockup .brand-name {
    position: absolute; top: 22px; font-size: 16px;
  }
  .strip-lockup .label-copy {
    position: absolute; top: 42px;
    text-align: right; font-size: 4.8px; line-height: 1.05;
  }
  .strip-lockup .emblem { top: 16px; width: 64px; height: 64px; }

  .strip-lockup.is-light .brand-name,
  .strip-lockup.is-light .label-copy { right: calc(916px - 205px); }
  .strip-lockup.is-light .emblem { left: 216px; }

  .strip-lockup.is-dark .brand-name,
  .strip-lockup.is-dark .label-copy { right: calc(916px - 775px); }
  .strip-lockup.is-dark .emblem { left: 784px; }
</style>
</head>
<body>
<main class="artboard">

  <section class="lockup-horizontal" aria-label="Horizontal logo lockup">
    <h1 class="brand-name">Gloam e-Liquid</h1>
    <p class="label-copy"><strong>Warning</strong>Keep away from children and pets.<br>May be harmful if swallowed<br>Ingredients: Propylene Glycol, Vegetable Glycerin,<br>Natural and Artificial Flavor, (number)mg Nicotine. The<br>name of the specific liquid.</p>
    <span class="emblem" aria-hidden="true"></span>
  </section>

  <section class="lockup-stacked" aria-label="Stacked logo lockup">
    <span class="emblem" aria-hidden="true"></span>
    <h2 class="brand-name">Gloam e-Liquid</h2>
    <p class="label-copy"><strong>Warning</strong>Keep away from children and pets.<br>May be harmful if swallowed<br>Ingredients: Propylene Glycol, Vegetable Glycerin,<br>Natural and Artificial Flavor, (number)mg Nicotine. The<br>name of the specific liquid.</p>
  </section>

  <section class="label-strip is-red" aria-label="Red label">
    <div class="strip-lockup is-light">
      <p class="brand-name">Gloam e-Liquid</p>
      <p class="label-copy"><strong>Warning</strong>Keep away from children and pets.<br>May be harmful if swallowed<br>Ingredients: Propylene Glycol, Vegetable Glycerin,<br>Natural and Artificial Flavor, (number)mg Nicotine. The<br>name of the specific liquid.</p>
      <span class="emblem" aria-hidden="true"></span>
    </div>
    <div class="strip-lockup is-dark">
      <p class="brand-name">Gloam e-Liquid</p>
      <p class="label-copy"><strong>Warning</strong>Keep away from children and pets.<br>May be harmful if swallowed<br>Ingredients: Propylene Glycol, Vegetable Glycerin,<br>Natural and Artificial Flavor, (number)mg Nicotine. The<br>name of the specific liquid.</p>
      <span class="emblem" aria-hidden="true"></span>
    </div>
  </section>

  <section class="label-strip is-green" aria-label="Green label">
    <div class="strip-lockup is-light">
      <p class="brand-name">Gloam e-Liquid</p>
      <p class="label-copy"><strong>Warning</strong>Keep away from children and pets.<br>May be harmful if swallowed<br>Ingredients: Propylene Glycol, Vegetable Glycerin,<br>Natural and Artificial Flavor, (number)mg Nicotine. The<br>name of the specific liquid.</p>
      <span class="emblem" aria-hidden="true"></span>
    </div>
    <div class="strip-lockup is-dark">
      <p class="brand-name">Gloam e-Liquid</p>
      <p class="label-copy"><strong>Warning</strong>Keep away from children and pets.<br>May be harmful if swallowed<br>Ingredients: Propylene Glycol, Vegetable Glycerin,<br>Natural and Artificial Flavor, (number)mg Nicotine. The<br>name of the specific liquid.</p>
      <span class="emblem" aria-hidden="true"></span>
    </div>
  </section>

  <section class="label-strip is-navy" aria-label="Navy label">
    <div class="strip-lockup is-light">
      <p class="brand-name">Gloam e-Liquid</p>
      <p class="label-copy"><strong>Warning</strong>Keep away from children and pets.<br>May be harmful if swallowed<br>Ingredients: Propylene Glycol, Vegetable Glycerin,<br>Natural and Artificial Flavor, (number)mg Nicotine. The<br>name of the specific liquid.</p>
      <span class="emblem" aria-hidden="true"></span>
    </div>
    <div class="strip-lockup is-dark">
      <p class="brand-name">Gloam e-Liquid</p>
      <p class="label-copy"><strong>Warning</strong>Keep away from children and pets.<br>May be harmful if swallowed<br>Ingredients: Propylene Glycol, Vegetable Glycerin,<br>Natural and Artificial Flavor, (number)mg Nicotine. The<br>name of the specific liquid.</p>
      <span class="emblem" aria-hidden="true"></span>
    </div>
  </section>

</main>
</body>
</html>
```